Packaging design for a revolutionary hi-protein snack of Norwegian salmon

We need a breathtaking packing design for a smal snack bag (30 g) for a revolutionary new hi-protein snack made of Norwegian salmon. The product will be made with two different flavors; MANGO and WASABI. The product is extreme high in protein (60%) and omega 3, and are just natural.

We want to see a bold and fresh design that appeals to protein lovers of all ages.

Target Market(s)

Our target market is boys and girls that are 18-35 years old and that are interested in working out and eating healthy.

Industry/Entity Type

Snack industry (functional food, healthy snack, protein snack)

Font styles to use
Sans Serif

Requirements
Must have
• The package design must give the customer a WOW feeling. "HI-PROTEIN SNACK" must be highligted. Further, the design must use the Tidal Compass setup (attached).

```html
<!DOCTYPE html>
<html lang="en">
<head>
<meta charset="utf-8">
<title>Hi-Protein Fish Snack Packaging</title>
<link rel="stylesheet" href="https://fonts.googleapis.com/css2?family=Outfit:wght@500;800&family=Oswald:wght@400;500&display=swap">
<style>
  :root {
    --bg: #fcc600;
    --navy: #1f2a5e;
    --red-o: #d8334a;
    --silver-1: #e9e9ec;
    --silver-2: #f8f8fa;
    --silver-3: #cfcfd4;
    --crimp: #b9b6bb;
    --white: #ffffff;
  }
  * { box-sizing: border-box; margin: 0; padding: 0; }
  html, body { width: 1200px; height: 1101px; overflow: hidden; background: var(--bg); }
  .canvas { position: relative; width: 1200px; height: 1101px; }

  .bag {
    position: absolute; width: 324px; height: 482px; overflow: hidden;
    background: linear-gradient(100deg, var(--silver-3) 0%, var(--silver-2) 18%, var(--silver-1) 45%, var(--silver-2) 70%, var(--silver-3) 100%);
  }
  .bag--green  { --stripe: #1f9c82; --accent: #17806a; }
  .bag--blue   { --stripe: #90afd6; --accent: #6f8cb8; }
  .bag--red    { --stripe: #d8495d; --accent: #c93a4d; }
  .bag--cyan   { --stripe: #33b5d2; --accent: #1fa3c4; }
  .bag--sage   { --stripe: #80b795; --accent: #6aa883; }
  .bag--olive  { --stripe: #8fb46a; --accent: #86b35a; }

  .bag__stripe { position: absolute; left: 195px; top: 0; width: 129px; height: 100%; background: var(--stripe); }
  .bag__edge { position: absolute; right: 0; top: 0; width: 7px; height: 100%; background: #2a3fa0; }
  .bag__crimp {
    position: absolute; left: 0; width: 100%; height: 27px; z-index: 3;
    background: repeating-linear-gradient(180deg, rgba(255,255,255,.35) 0 2px, rgba(0,0,0,.12) 2px 4px), var(--crimp);
    opacity: .85;
  }
  .bag__crimp--top { top: 0; }
  .bag__crimp--bottom { bottom: 0; }
  .bag__hole { position: absolute; left: 130px; top: 16px; width: 68px; height: 12px; border-radius: 6px; background: var(--bg); z-index: 4; }

  .rot { position: absolute; transform: rotate(-90deg); transform-origin: center; white-space: nowrap; z-index: 2; }

  .product-name {
    left: -95px; top: 213px; width: 298px; height: 68px;
    font: 800 84px/68px "Outfit", sans-serif; letter-spacing: -2px; color: var(--navy); text-align: center;
  }
  .product-name .o { color: var(--red-o); }
  .bag--cod .product-name { left: -78px; top: 206px; width: 264px; font-size: 96px; }

  .product-type {
    position: absolute; left: 24px; top: 398px; z-index: 2;
    font: 800 60px/1 "Outfit", sans-serif; letter-spacing: -1.5px; color: var(--accent);
  }
  .bag--cod .product-type { top: 384px; left: 20px; font-size: 58px; }

  .claim {
    left: 68px; top: 254px; width: 120px; height: 57px;
    font: 500 26px/28px "Oswald", sans-serif; color: var(--accent); text-align: right;
  }
  .bag--cod .claim { top: 271px; }

  .stats {
    position: absolute; left: 104px; top: 362px; z-index: 2; white-space: nowrap;
    font: 500 15px/20px "Oswald", sans-serif; letter-spacing: -0.4px; color: var(--navy);
  }
  .bag--cod .stats { top: 356px; }

  .origin {
    left: 100px; top: 106px; width: 100px; height: 40px;
    font: 500 15px/18px "Outfit", sans-serif; color: var(--navy); letter-spacing: 1px;
    display: flex; align-items: center; gap: 6px;
  }
  .origin__mark { width: 8px; height: 8px; background: var(--red-o); flex: none; }
  .bag--cod .origin { top: 110px; }

  .brand {
    position: absolute; left: 207px; top: 94px; width: 110px; z-index: 2;
    font: 800 25px/24px "Outfit", sans-serif; color: var(--white); text-align: center;
  }
  .bag--cod .brand { top: 96px; }

  .desc { position: absolute; left: 207px; top: 288px; z-index: 2; font: 400 10.5px/15px "Oswald", sans-serif; color: var(--white); }
  .bag--cod .desc { top: 290px; }

  .photo { position: absolute; z-index: 1; }
  .photo--bites { left: 185px; top: 175px; width: 134px; height: 90px; border-radius: 40% 30% 45% 35%; background: radial-gradient(circle at 45% 45%, #d9743e, #b6532a 70%); }
  .photo--steak { left: 192px; top: 362px; width: 126px; height: 92px; border-radius: 50% 40% 20% 30%; background: radial-gradient(circle at 40% 40%, #f6a07c, #e8805a 60%, #cfcbc6 90%); }
  .photo--chips { left: 168px; top: 158px; width: 142px; height: 132px; border-radius: 45%; background: radial-gradient(circle at 45% 40%, #ffe36a, #f2c22a 70%); }
  .photo--fillet { left: 192px; top: 362px; width: 124px; height: 84px; border-radius: 30% 45% 25% 40%; background: radial-gradient(circle at 40% 50%, #f3e6d2, #d9a46c 80%); }
</style>
</head>
<body>
<main class="canvas">

  <section class="bag bag--green bag--salmon" style="left:43px;top:45px">
    <div class="bag__stripe"></div>
    <div class="bag__crimp bag__crimp--top"></div><div class="bag__crimp bag__crimp--bottom"></div>
    <div class="bag__hole"></div>
    <div class="rot product-name">Salm<span class="o">o</span>n</div>
    <div class="rot claim">HI-PROTEIN<br>SNACK</div>
    <div class="rot origin"><span>TIDAL<br>COMPASS</span><span class="origin__mark"></span></div>
    <div class="stats">80% PROTEIN,<br>2% CARBS</div>
    <div class="product-type">bites</div>
    <div class="brand">Four<br>Factors</div>
    <div class="photo photo--bites" role="img" aria-label="Dehydrated salmon bites"></div>
    <p class="desc">Natural dehydrated<br>bites of Salmon meat<br>with delicious flavors</p>
    <div class="photo photo--steak" role="img" aria-label="Fresh salmon steak"></div>
  </section>

  <section class="bag bag--blue bag--salmon" style="left:432px;top:45px">
    <div class="bag__stripe"></div>
    <div class="bag__crimp bag__crimp--top"></div><div class="bag__crimp bag__crimp--bottom"></div>
    <div class="bag__hole"></div>
    <div class="rot product-name">Salm<span class="o">o</span>n</div>
    <div class="rot claim">HI-PROTEIN<br>SNACK</div>
    <div class="rot origin"><span>TIDAL<br>COMPASS</span><span class="origin__mark"></span></div>
    <div class="stats">80% PROTEIN,<br>2% CARBS</div>
    <div class="product-type">bites</div>
    <div class="brand">Four<br>Factors</div>
    <div class="photo photo--bites" role="img" aria-label="Dehydrated salmon bites"></div>
    <p class="desc">Natural dehydrated<br>bites of Salmon meat<br>with delicious flavors</p>
    <div class="photo photo--steak" role="img" aria-label="Fresh salmon steak"></div>
  </section>

  <section class="bag bag--red bag--salmon" style="left:821px;top:45px">
    <div class="bag__stripe"></div>
    <div class="bag__crimp bag__crimp--top"></div><div class="bag__crimp bag__crimp--bottom"></div>
    <div class="bag__hole"></div>
    <div class="rot product-name">Salm<span class="o">o</span>n</div>
    <div class="rot claim">HI-PROTEIN<br>SNACK</div>
    <div class="rot origin"><span>TIDAL<br>COMPASS</span><span class="origin__mark"></span></div>
    <div class="stats">80% PROTEIN,<br>2% CARBS</div>
    <div class="product-type">bites</div>
    <div class="brand">Four<br>Factors</div>
    <div class="photo photo--bites" role="img" aria-label="Dehydrated salmon bites"></div>
    <p class="desc">Natural dehydrated<br>bites of Salmon meat<br>with delicious flavors</p>
    <div class="photo photo--steak" role="img" aria-label="Fresh salmon steak"></div>
  </section>

  <section class="bag bag--cyan bag--cod" style="left:43px;top:569px">
    <div class="bag__stripe"></div><div class="bag__edge"></div>
    <div class="bag__crimp bag__crimp--top"></div><div class="bag__crimp bag__crimp--bottom"></div>
    <div class="bag__hole"></div>
    <div class="rot product-name">C<span class="o">o</span>d</div>
    <div class="rot claim">HI-PROTEIN<br>SNACK</div>
    <div class="rot origin"><span>TIDAL<br>COMPASS</span><span class="origin__mark"></span></div>
    <div class="stats">80% PROTEIN,<br>2% CARBS</div>
    <div class="product-type">Chips</div>
    <div class="brand">Four<br>Factors</div>
    <div class="photo photo--chips" role="img" aria-label="Crinkle-cut cod chips"></div>
    <p class="desc">Natural dehydrated<br>bites of Salmon meat<br>with delicious flavors</p>
    <div class="photo photo--fillet" role="img" aria-label="Grilled cod fillet"></div>
  </section>

  <section class="bag bag--sage bag--cod" style="left:432px;top:569px">
    <div class="bag__stripe"></div><div class="bag__edge"></div>
    <div class="bag__crimp bag__crimp--top"></div><div class="bag__crimp bag__crimp--bottom"></div>
    <div class="bag__hole"></div>
    <div class="rot product-name">C<span class="o">o</span>d</div>
    <div class="rot claim">HI-PROTEIN<br>SNACK</div>
    <div class="rot origin"><span>TIDAL<br>COMPASS</span><span class="origin__mark"></span></div>
    <div class="stats">80% PROTEIN,<br>2% CARBS</div>
    <div class="product-type">Chips</div>
    <div class="brand">Four<br>Factors</div>
    <div class="photo photo--chips" role="img" aria-label="Crinkle-cut cod chips"></div>
    <p class="desc">Natural dehydrated<br>bites of Salmon meat<br>with delicious flavors</p>
    <div class="photo photo--fillet" role="img" aria-label="Grilled cod fillet"></div>
  </section>

  <section class="bag bag--olive bag--cod" style="left:821px;top:569px">
    <div class="bag__stripe"></div><div class="bag__edge"></div>
    <div class="bag__crimp bag__crimp--top"></div><div class="bag__crimp bag__crimp--bottom"></div>
    <div class="bag__hole"></div>
    <div class="rot product-name">C<span class="o">o</span>d</div>
    <div class="rot claim">HI-PROTEIN<br>SNACK</div>
    <div class="rot origin"><span>TIDAL<br>COMPASS</span><span class="origin__mark"></span></div>
    <div class="stats">80% PROTEIN,<br>2% CARBS</div>
    <div class="product-type">Chips</div>
    <div class="brand">Four<br>Factors</div>
    <div class="photo photo--chips" role="img" aria-label="Crinkle-cut cod chips"></div>
    <p class="desc">Natural dehydrated<br>bites of Salmon meat<br>with delicious flavors</p>
    <div class="photo photo--fillet" role="img" aria-label="Grilled cod fillet"></div>
  </section>

</main>
</body>
</html>
```